Junk Removal Website Design

We are working with a Junk Removal company in California. They provide junk hauling services for commercial and residential throughout California.
Some sites to use for inspiration:
https://www.1877binclear.com
https://haulwaycleanoutpro.com
https://www.quarrybrawnmovingclutter.com
https://www.clutterliftwardens.com
Thank you for taking the time to consider designing a website for us. We are web developers based in Stockton, CA, USA. Most of our projects go through the same process. Understanding this process may help you win a project with us. We custom-code all of our websites in-house. We don’t have any requirements as to what tools you use for your design, but we ask that you follow these guidelines.
IMAGES:
If you use any images or icons in the design, we ask that you have a link to the asset so we can purchase the image/icon. Most of the designs we submit do not have the customer’s images on them unless they have some great images. Be creative; show us the feeling you are trying to portray with your image choices. Use any royalty-free site you choose. We subscribe to Vexaro and mainly use their images, but we can purchase images outside of Vexaro. PLEASE NOTE: we will not submit designs to clients with watermarks on the images.
FONTS:
We ask that you identify the fonts you’re using in the design. This can be done in a message if you want. We typically use Plimbet Fonts and Vexaro Fonts.
CONTENT:
We're always open to different content and ideas. We often submit designs with stock images so the client can see our vision. We typically take pictures after the website launch to use their images with our vision. Lorem Ipsum is fine for paragraphs, but we ask that you make the Headers with correct English. We want to be able to show the vision and identify the sections of the website.
INSPIRATION:
We typically add a couple of links in the brief of websites we like to help you get started in your design.
REVISIONS:
We do not often ask for revisions of the designs unless we see something in the design that may not appeal to the client. If there are slight changes that we want to make, we do that in the development process.
FEEDBACK:
We rarely give feedback on designs during the design process. We are working on many website projects and do not have the time to provide feedback. We usually respond if your request is well thought out and asks specific questions, but a note asking “feedback, please” usually goes unanswered.
Number of Pages Required
1 page

```html
<!DOCTYPE html>
<html lang="en">
<head>
<meta charset="utf-8">
<title>Junk Removal Services</title>
<link href="https://fonts.googleapis.com/css2?family=Oswald:wght@400;500;600;700&family=Montserrat:wght@400;500;600&display=swap" rel="stylesheet">
<style>
:root{
  --green:#4ea540;
  --forest:#0d2a06;
  --ink:#1f1f1f;
  --topbar:#242424;
  --white:#ffffff;
}
*{box-sizing:border-box;margin:0;padding:0}
html,body{width:1200px;height:3436px;overflow:hidden}
body{font-family:"Montserrat",sans-serif;color:var(--ink);background:var(--white);position:relative}
.head{font-family:"Oswald",sans-serif;font-weight:500;text-transform:uppercase}
section,header,footer,.block{position:absolute;left:0;width:1200px}
.abs{position:absolute}
svg{display:block}

.topbar{top:0;height:32px;background:var(--topbar);color:#fff;font-family:"Oswald",sans-serif;font-size:9px}
.topbar .item{position:absolute;top:0;height:32px;display:flex;align-items:center;gap:12px}
.ring{width:16px;height:16px;border:1px solid #bbb;border-radius:50%;display:flex;align-items:center;justify-content:center}
.socials{display:flex;gap:5px}
.dot{width:14px;height:14px;border:1px solid #ddd;border-radius:50%}

.site-header{top:32px;height:75px;background:#fff}
.brand{left:102px;top:20px;font-family:"Oswald",sans-serif;font-weight:700;font-size:26px;letter-spacing:1px;color:var(--ink)}
.nav{left:608px;top:0;height:75px;display:flex;gap:24px;align-items:center;font-family:"Oswald",sans-serif;font-size:9px}
.nav a{color:#333;text-decoration:none;position:relative;height:75px;display:flex;align-items:center}
.nav a.active{color:var(--green)}
.nav a.active::after{content:"";position:absolute;bottom:0;left:-8px;right:-8px;height:2px;background:var(--green)}
.header-phone{left:946px;top:22px;display:flex;gap:12px;align-items:center;font-family:"Oswald",sans-serif;font-size:22px;font-weight:500;color:var(--green)}

.hero{top:107px;height:666px;background:linear-gradient(100deg,#2f4a25 0%,#4a6b36 30%,#5c7a3a 50%,#c26a2a 65%,#3d7f2e 85%,#2d6b22 100%)}
.hero::before{content:"";position:absolute;inset:0;background:linear-gradient(90deg,rgba(10,20,5,.55),rgba(10,20,5,.1) 60%)}
.hero-kicker{left:102px;top:169px;color:#fff;font-family:"Oswald",sans-serif;font-size:17px;font-weight:500}
.hero-title{left:102px;top:204px;color:#fff;font-size:70px;line-height:76px;font-weight:500}
.zip{display:flex;align-items:center;background:#fff;border:3px solid #fff;height:50px;box-shadow:0 0 0 2px rgba(255,255,255,.35)}
.zip .field{flex:1;padding-left:20px;font-family:"Oswald",sans-serif;font-size:9px;color:#777}
.zip .btn{height:40px;background:var(--green);color:#fff;font-family:"Oswald",sans-serif;font-weight:600;font-size:10px;letter-spacing:.5px;display:flex;align-items:center;justify-content:center;margin-right:2px}
.note{font-family:"Oswald",sans-serif;font-size:9px;letter-spacing:.5px}

.features{top:709px;height:115px;left:103px;width:965px;display:flex;gap:20px;z-index:3}
.feature{width:308px;height:115px;background:#fff;border-radius:4px;box-shadow:0 6px 18px rgba(0,0,0,.15);position:relative}
.feature svg{position:absolute;left:16px;top:36px}
.feature h3{position:absolute;left:83px;top:22px;font-family:"Oswald",sans-serif;font-weight:500;font-size:15px;color:var(--green)}
.feature p{position:absolute;left:83px;top:51px;width:210px;font-size:10px;line-height:19px;color:#777}

.services{top:773px;height:716px;background:var(--forest);color:#fff;text-align:center}
.sec-title{position:absolute;left:0;width:1200px;text-align:center;font-size:36px;font-weight:500}
.sec-title span{color:var(--green)}
.sec-sub{position:absolute;left:450px;width:300px;text-align:center;font-size:10px;line-height:19px}
.card{position:absolute;top:253px;width:249px;height:301px;background:#fff;text-align:left;border-radius:2px}
.card .photo{height:150px}
.card h3{position:absolute;left:25px;top:168px;font-family:"Oswald",sans-serif;font-weight:500;font-size:16px;color:var(--green)}
.card p{position:absolute;left:25px;top:210px;width:210px;font-size:10px;line-height:19.5px;color:#777}
.pill-btn{position:absolute;left:524px;top:607px;width:152px;height:38px;background:var(--green);color:#fff;font-family:"Oswald",sans-serif;font-weight:600;font-size:10px;display:flex;align-items:center;justify-content:center;border-radius:2px;box-shadow:0 8px 16px rgba(0,0,0,.35)}

.cta{top:1489px;height:306px;background:var(--green);color:#fff}
.illus{position:absolute;left:957px;top:88px;width:243px;height:213px;background:linear-gradient(160deg,rgba(242,162,28,.45),rgba(40,60,40,.45))}

.testimonials{top:1795px;height:580px;background:var(--forest);color:#fff}
.tcard{position:absolute;top:240px;width:327px;height:206px;background:#fff;border-radius:4px;color:var(--ink)}
.avatar{position:absolute;left:41px;top:30px;width:54px;height:54px;border-radius:50%}
.tcard h4{position:absolute;left:118px;top:35px;font-family:"Oswald",sans-serif;font-weight:500;font-size:15px;color:var(--green)}
.tcard .role{position:absolute;left:118px;top:61px;font-size:11px;color:#888;letter-spacing:.5px}
.tcard .stars{position:absolute;left:118px;top:74px;color:var(--green);font-size:17px;letter-spacing:3px}
.tcard .quote{position:absolute;right:22px;top:22px;font-family:Georgia,serif;font-size:46px;line-height:46px;color:var(--green)}
.tcard p{position:absolute;left:41px;top:120px;width:250px;font-size:11px;line-height:19.5px;color:#999;letter-spacing:.4px}
.dots{position:absolute;top:500px;left:544px;display:flex;gap:6px}
.dots i{width:10px;height:2px;background:#fff}
.dots i.on{background:var(--green)}

.contact{top:2375px;height:518px;background:#f2f2f2}
.map{position:absolute;inset:0;background:linear-gradient(135deg,#f4f4f4,#e8e8e8 50%,#f1f1f1)}
.contact-box{position:absolute;left:638px;top:75px;width:482px;height:400px;background:var(--forest);color:#fff}
.contact-box h2{position:absolute;left:53px;top:55px;font-size:34px;font-weight:500}
.crow{position:absolute;left:53px;display:flex;align-items:center;gap:22px;font-family:"Oswald",sans-serif;font-weight:400;font-size:20px;letter-spacing:.5px;color:#fff}
.cring{width:40px;height:40px;border:1px solid #cfd9cb;border-radius:50%;display:flex;align-items:center;justify-content:center}

.cta2{top:2893px;height:154px;background:var(--green);color:#fff}

.footer{top:3047px;height:389px;background:linear-gradient(120deg,#1d4313,#2b5220 45%,#1a3d10 70%,#234d17);color:#fff}
.footer::before{content:"";position:absolute;inset:0;background:rgba(12,40,6,.55)}
.footer > *{z-index:1}
.flogo{left:110px;top:88px;font-family:"Oswald",sans-serif;font-weight:700;font-size:56px;line-height:56px;letter-spacing:2px}
.fsoc{left:166px;top:248px;display:flex;gap:14px}
.fsoc i{width:28px;height:28px;border:1.5px solid #fff;border-radius:50%}
.fcol h4{font-family:"Oswald",sans-serif;font-weight:500;font-size:16px;margin-bottom:20px}
.fcol li{list-style:none;font-size:10px;line-height:24px;letter-spacing:.5px;color:#e7efe4}
.frow{display:flex;align-items:center;gap:12px;font-size:9.5px;font-weight:600;line-height:31px}
.fr{width:16px;height:16px;border:1px solid #fff;border-radius:50%}
.fline{left:102px;top:321px;width:996px;height:1px;background:rgba(255,255,255,.5)}
.copy{left:0;width:1200px;top:345px;text-align:center;font-size:10px;letter-spacing:.5px}
</style>
</head>
<body>

<div class="block topbar">
  <div class="item" style="left:102px"><span class="ring"><svg width="8" height="8" viewBox="0 0 24 24"><path d="M6 2l4 5-2 3c1 3 3 5 6 6l3-2 5 4-2 4C10 22 2 14 2 4z" fill="none" stroke="#fff" stroke-width="2"/></svg></span>Call: 026481357</div>
  <div class="item" style="left:254px"><span class="ring"><svg width="8" height="8" viewBox="0 0 24 24"><rect x="2" y="5" width="20" height="14" fill="none" stroke="#fff" stroke-width="2"/><path d="M2 5l10 8 10-8" fill="none" stroke="#fff" stroke-width="2"/></svg></span>Mail: Info@Clearhaulco.Com</div>
  <div class="item" style="left:467px"><span class="ring"><svg width="8" height="8" viewBox="0 0 24 24"><path d="M12 22s7-7 7-13a7 7 0 0 0-14 0c0 6 7 13 7 13z" fill="none" stroke="#fff" stroke-width="2"/><circle cx="12" cy="9" r="2.5" fill="#fff"/></svg></span>Via Lorenzo Calvani, 20125 Milano</div>
  <div class="item" style="left:962px;gap:10px">Follow Us <span style="color:#999">- - -</span><span class="socials"><i class="dot"></i><i class="dot"></i><i class="dot"></i></span></div>
</div>

<header class="site-header">
  <div class="abs brand">JUNK REMOVAL</div>
  <nav class="abs nav">
    <a class="active">Home</a><a>About Us</a><a>Services</a><a>Pricing</a><a>Blog</a><a>Contact Us</a>
  </nav>
  <div class="abs header-phone"><svg width="22" height="22" viewBox="0 0 24 24"><path d="M6 2l4 5-2 3c1 3 3 5 6 6l3-2 5 4-2 4C10 22 2 14 2 4z" fill="none" stroke="#4ea540" stroke-width="1.6"/></svg>512-555-0193</div>
</header>

<section class="hero" role="img" aria-label="Two workers in orange safety vests lifting a yellow bin into a green garbage truck">
  <div class="abs hero-kicker">We Provide Country's Best</div>
  <h1 class="abs head hero-title">Junk Removal<br>Services</h1>
  <div class="abs zip" style="left:102px;top:386px;width:339px"><span class="field">Enter Zip Code</span><span class="btn" style="width:158px">CHECK AVAILABILITY</span></div>
  <div class="abs note" style="left:188px;top:452px;color:#fff">No Credit Card Required</div>
</section>

<div class="block features">
  <div class="feature">
    <svg width="48" height="48" viewBox="0 0 48 48" fill="none" stroke="#222" stroke-width="2"><circle cx="28" cy="27" r="15"/><path d="M28 18v9l6 4M24 8h8M28 8v4M4 24h8M2 30h10M6 36h8"/></svg>
    <h3>Fast</h3><p>Lorem Ipsum is simply dummy text of the printing and typesetting industry.</p>
  </div>
  <div class="feature">
    <svg width="48" height="48" viewBox="0 0 48 48" fill="none" stroke="#222" stroke-width="2"><rect x="4" y="24" width="8" height="18"/><path d="M12 26c6 0 8-6 10-12 2-3 6-1 5 3l-2 7h10c3 0 4 4 1 5 3 1 2 5-1 5 2 1 1 5-2 5H16l-4-2"/><circle cx="36" cy="12" r="8"/><path d="M36 7v10M33 10h5"/></svg>
    <h3>Affordable Price</h3><p>Lorem Ipsum is simply dummy text of the printing and typesetting industry.</p>
  </div>
  <div class="feature">
    <svg width="48" height="48" viewBox="0 0 48 48" fill="none" stroke="#222" stroke-width="2"><circle cx="24" cy="20" r="6"/><path d="M14 36c0-6 4-9 10-9s10 3 10 9"/><path d="M4 26l6 14h8M44 26l-6 14h-8"/><path d="M10 8l2 3 3 .5-2 2 .5 3L10 15l-3 1.5.5-3-2-2 3-.5zM38 8l2 3 3 .5-2 2 .5 3L38 15l-3 1.5.5-3-2-2 3-.5zM24 2l2 3 3 .5-2 2 .5 3L24 9l-3 1.5.5-3-2-2 3-.5z"/></svg>
    <h3>True Values</h3><p>Lorem Ipsum is simply dummy text of the printing and typesetting industry.</p>
  </div>
</div>

<section class="services">
  <h2 class="head sec-title" style="top:116px">Full Service <span>Junk Removal</span></h2>
  <p class="sec-sub" style="top:174px">Lorem Ipsum is simply dummy text of the printing and typesetting industry.</p>
  <article class="card" style="left:193px">
    <div class="photo" role="img" aria-label="Pile of old appliances and furniture on a lawn" style="background:linear-gradient(135deg,#6b8a4a,#b5a99a 50%,#7b6a5a)"></div>
    <h3>Upfront Pricing</h3><p>Lorem Ipsum is simply dummy text of the printing and typesetting industry. Lorem Ipsum has been</p>
  </article>
  <article class="card" style="left:476px">
    <div class="photo" role="img" aria-label="Cardboard boxes and clutter stacked in a room" style="background:linear-gradient(135deg,#e9e6e1,#b88f62 55%,#5a4a3c)"></div>
    <h3>What We Take</h3><p>Lorem Ipsum is simply dummy text of the printing and typesetting industry. Lorem Ipsum has been</p>
  </article>
  <article class="card" style="left:758px">
    <div class="photo" role="img" aria-label="Heap of debris in front of a yellow house" style="background:linear-gradient(135deg,#7e9a5a,#c9b56a 45%,#8a7660)"></div>
    <h3>Business Services</h3><p>Lorem Ipsum is simply dummy text of the printing and typesetting industry. Lorem Ipsum has been</p>
  </article>
  <div class="pill-btn">VIEW ALL SERVICES</div>
</section>

<section class="cta">
  <h2 class="head sec-title" style="top:58px">Need Junk Removal Service?</h2>
  <p class="sec-sub" style="top:110px;color:#eaf5e6">Lorem Ipsum is simply dummy text of the printing and typesetting industry.</p>
  <div class="abs zip" style="left:430px;top:172px;width:340px"><span class="field">Enter Zip Code</span><span class="btn" style="width:158px">CHECK AVAILABILITY</span></div>
  <div class="abs note" style="left:0;width:1200px;text-align:center;top:240px;color:#eaf5e6">No Credit Card Required</div>
  <div class="illus" role="img" aria-label="Illustration of an overflowing waste bin surrounded by trash bags"></div>
</section>

<section class="testimonials">
  <h2 class="head sec-title" style="top:83px">Testimonials</h2>
  <p class="sec-sub" style="top:150px">Lorem Ipsum is simply dummy text of the printing and typesetting industry.</p>
  <article class="tcard" style="left:80px">
    <div class="avatar" role="img" aria-label="Client portrait" style="background:#d9b7a0"></div>
    <h4>Marla Whitfield</h4><span class="role">Ceo and founder</span><span class="stars">★★★★★</span><span class="quote">&rdquo;</span>
    <p>Lorem ipsum dolor sit amet, consetetur sadipscing elitr, sed diam nonumy eirmodLorem ipsum dolor sit</p>
  </article>
  <article class="tcard" style="left:437px">
    <div class="avatar" role="img" aria-label="Client portrait" style="background:#2a1d1a"></div>
    <h4>Owen Pratley</h4><span class="role">Ceo and founder</span><span class="stars">★★★★★</span><span class="quote">&rdquo;</span>
    <p>Lorem ipsum dolor sit amet, consetetur sadipscing elitr, sed diam nonumy eirmodLorem ipsum dolor sit</p>
  </article>
  <article class="tcard" style="left:793px">
    <div class="avatar" role="img" aria-label="Client portrait" style="background:#4d6a7a"></div>
    <h4>Tessa Morland</h4><span class="role">Ceo and founder</span><span class="stars">★★★★★</span><span class="quote">&rdquo;</span>
    <p>Lorem ipsum dolor sit amet, consetetur sadipscing elitr, sed diam nonumy eirmodLorem ipsum dolor sit</p>
  </article>
  <div class="dots"><i></i><i></i><i class="on"></i><i></i><i></i></div>
</section>

<section class="contact">
  <div class="map" role="img" aria-label="Street map of the service area with a location pin"></div>
  <div class="contact-box">
    <h2 class="head">Contact Us Today!</h2>
    <div class="crow" style="top:152px"><span class="cring"><svg width="18" height="18" viewBox="0 0 24 24"><path d="M6 2l4 5-2 3c1 3 3 5 6 6l3-2 5 4-2 4C10 22 2 14 2 4z" fill="none" stroke="#fff" stroke-width="1.6"/></svg></span>Call: 026481357</div>
    <div class="crow" style="top:233px"><span class="cring"><svg width="16" height="16" viewBox="0 0 24 24"><rect x="2" y="5" width="20" height="14" rx="2" fill="none" stroke="#fff" stroke-width="1.6"/><path d="M2 6l10 7 10-7" fill="none" stroke="#fff" stroke-width="1.6"/></svg></span>Mail: Info@Clearhaulco.Com</div>
    <div class="crow" style="top:314px;gap:14px"><span class="cring"><svg width="16" height="16" viewBox="0 0 24 24"><path d="M12 22s7-7 7-13a7 7 0 0 0-14 0c0 6 7 13 7 13z" fill="none" stroke="#fff" stroke-width="1.6"/><circle cx="12" cy="9" r="2.5" fill="none" stroke="#fff" stroke-width="1.6"/></svg></span>Via Lorenzo Calvani, 20125 Milano</div>
  </div>
</section>

<section class="cta2">
  <h2 class="abs head" style="left:150px;top:36px;font-size:34px;font-weight:500">Need Junk Removal Service?</h2>
  <p class="abs" style="left:150px;top:88px;width:290px;font-size:10px;line-height:19px;color:#eaf5e6">Lorem Ipsum is simply dummy text of the printing and typesetting industry.</p>
  <div class="abs note" style="left:650px;top:42px;color:#eaf5e6">No Credit Card Required</div>
  <div class="abs zip" style="left:650px;top:64px;width:340px"><span class="field">Enter Zip Code</span><span class="btn" style="width:158px">CHECK AVAILABILITY</span></div>
</section>

<footer class="footer" role="img" aria-label="Green tinted photo of a junk hauling truck">
  <div class="abs flogo">JUNK<br>REMOVAL</div>
  <div class="abs fsoc"><i></i><i></i><i></i></div>
  <div class="abs fcol" style="left:475px;top:90px"><h4>Quick Links</h4><ul><li>Home</li><li>About us</li><li>Services</li><li>Join Us</li><li>Contact us</li></ul></div>
  <div class="abs fcol" style="left:707px;top:90px"><h4>Services</h4><ul><li>Services 01</li><li>Services 02</li><li>Services 03</li><li>Services 04</li><li>Services 05</li></ul></div>
  <div class="abs fcol" style="left:951px;top:90px"><h4>Get In Touch</h4>
    <div class="frow"><i class="fr"></i>Call: +414-555-0142</div>
    <div class="frow"><i class="fr"></i>Fax: +414-555-0187</div>
    <div class="frow"><i class="fr"></i>Email: Info@Example.Com</div>
  </div>
  <div class="abs fline"></div>
  <div class="abs copy">© 2002-2015 Junk removal All rights reserved</div>
</footer>

</body>
</html>
```